Brisk Comet- Energy shot - ....Amazing Energy for Amazing people

To design a creative /unique logo and picture for Brisk Comet Energy/ energy shot product similar to Zippo Day energy shot...Berry flavor

I want the design to cover the entire bottle. in addition to Logo (Brisk Comet Energy )

So Brisk Comet Energy will be a competitor of Zippo Day energy and I want a creative,fantastic, attractive design to catch customers eyes, the product will be in similar size 2oz bottle (see attached image). This template is based on a common 2oz bottle size that measures exactly 114mm circumference x 83mm-85mm height (including cap ).
Please include At the top cap a Logo for: Brisk Comet...

Target Market(s)

Young, busy professionals, athletics

Industry/Entity Type

Product

Logo Text

Quorva Energy...Amazing Energy &Taste !

Requirements
Must have
• Creative exciting design...Quorva Energy...Fan
Nice to have
• Be a genius....Be creative...Be Amazing !

```html
<!DOCTYPE html>
<html lang="en">
<head>
<meta charset="utf-8">
<title>Brisk Comet Energy – Bottle Label</title>
<link rel="stylesheet" href="https://fonts.googleapis.com/css2?family=Anton&family=Fjalla+One&family=Montserrat:wght@500&display=swap">
<style>
  :root {
    --page: #ffffff;
    --label-black: #121212;
    --label-charcoal: #2a2a2a;
    --flame-yellow: #ffd21a;
    --flame-orange: #f47a12;
    --flame-red: #c8140f;
    --band-red: #b3120e;
    --brand-orange: #f6a21f;
    --claim-yellow: #f7e01c;
    --figure-white: #f2f2f2;
    --fine-print: #d9d9d9;
  }
  * { margin: 0; padding: 0; box-sizing: border-box; }
  html, body {
    width: 1200px;
    height: 1200px;
    overflow: hidden;
    background: var(--page);
  }
  .canvas {
    position: relative;
    width: 1200px;
    height: 1200px;
  }
  .label {
    position: absolute;
    left: 100px;
    top: 150px;
    width: 1000px;
    height: 900px;
    overflow: hidden;
    background: radial-gradient(ellipse at 60% 45%, var(--label-charcoal) 0%, var(--label-black) 60%);
  }
  .label-bands {
    position: absolute;
    inset: 0;
  }
  .brand {
    position: absolute;
    left: 130px;
    top: 300px;
    font-family: "Anton", "Impact", sans-serif;
    font-weight: 400;
    color: var(--brand-orange);
    line-height: 1;
    text-transform: uppercase;
  }
  .brand-name {
    display: block;
    font-size: 150px;
    letter-spacing: 1px;
  }
  .brand-descriptor {
    display: block;
    margin-top: 6px;
    margin-left: 290px;
    font-size: 84px;
    letter-spacing: 4px;
  }
  .claims {
    position: absolute;
    left: 90px;
    top: 610px;
    list-style: none;
    font-family: "Fjalla One", "Arial Narrow", sans-serif;
    color: var(--claim-yellow);
    font-size: 34px;
    line-height: 1.12;
    transform: rotate(3deg);
    transform-origin: left top;
  }
  .claims li {
    display: flex;
    align-items: center;
    gap: 12px;
  }
  .claims svg { width: 26px; height: 26px; flex: none; }
  .runner-art {
    position: absolute;
    left: 560px;
    top: 540px;
    width: 360px;
    height: 360px;
    background: radial-gradient(ellipse at 50% 45%, var(--figure-white) 0%, #bdbdbd 55%, rgba(189,189,189,0) 72%);
  }
  .volume {
    position: absolute;
    right: 40px;
    bottom: 30px;
    font-family: "Montserrat", "Arial", sans-serif;
    font-weight: 500;
    font-size: 22px;
    color: var(--fine-print);
    letter-spacing: 1px;
  }
</style>
</head>
<body>
<main class="canvas">
  <section class="label">
    <svg class="label-bands" width="1000" height="900" viewBox="0 0 1000 900" aria-hidden="true">
      <defs>
        <linearGradient id="flameFill" x1="0" y1="0" x2="1" y2="1">
          <stop offset="0" stop-color="var(--flame-red)"/>
          <stop offset="0.35" stop-color="var(--flame-yellow)"/>
          <stop offset="0.65" stop-color="var(--flame-orange)"/>
          <stop offset="1" stop-color="var(--flame-red)"/>
        </linearGradient>
        <linearGradient id="lowerFlameFill" x1="0" y1="1" x2="1" y2="0">
          <stop offset="0" stop-color="var(--flame-red)"/>
          <stop offset="0.6" stop-color="var(--flame-orange)"/>
          <stop offset="1" stop-color="var(--flame-yellow)"/>
        </linearGradient>
      </defs>
      <path d="M0 0 H470 L0 470 Z" fill="var(--band-red)"/>
      <path d="M0 0 H430 L0 430 Z" fill="url(#flameFill)" role="img" aria-label="Swirling flame texture"/>
      <path d="M1000 650 V900 H760 Z" fill="var(--band-red)"/>
      <path d="M1000 700 V900 H810 Z" fill="url(#lowerFlameFill)" role="img" aria-label="Flame texture"/>
    </svg>

    <h1 class="brand">
      <span class="brand-name">Brisk Comet</span>
      <span class="brand-descriptor">Energy</span>
    </h1>

    <ul class="claims">
      <li><svg viewBox="0 0 24 24"><path d="M3 13 L9 19 L21 5" fill="none" stroke="currentColor" stroke-width="3.5" stroke-linecap="round" stroke-linejoin="round"/></svg>Hours of Energy Now</li>
      <li><svg viewBox="0 0 24 24"><path d="M3 13 L9 19 L21 5" fill="none" stroke="currentColor" stroke-width="3.5" stroke-linecap="round" stroke-linejoin="round"/></svg>No Crash Later</li>
      <li><svg viewBox="0 0 24 24"><path d="M3 13 L9 19 L21 5" fill="none" stroke="currentColor" stroke-width="3.5" stroke-linecap="round" stroke-linejoin="round"/></svg>Sugar Free</li>
      <li><svg viewBox="0 0 24 24"><path d="M3 13 L9 19 L21 5" fill="none" stroke="currentColor" stroke-width="3.5" stroke-linecap="round" stroke-linejoin="round"/></svg>0 Net Carbs</li>
    </ul>

    <div class="runner-art" role="img" aria-label="White silhouette of a sprinter bursting forward, breaking into shards"></div>

    <p class="volume">2 FL OZ (60ML)</p>
  </section>
</main>
</body>
</html>
```